Business Card Design

We need a business card to highlight our property maintenance company. we specialize in commercial and industrial property maintenance. services include landscaping snow and ice management. janitorial services. cleanroom services. parking lot maintenance.
Updates
I have narrowed down to two designs thank you waiting on some minor changes to both designs to choose.
Target Market(s)
facility managers/property managers
Industry/Entity Type
Property Maintenance
Contact Information for Business Card
47 Brimwell Rd.
Halden, Ma. 01472
978-552-7314
Look and feel
Each slider illustrates characteristics of the customer's brand and the style your logo design should communicate.

```html
<!DOCTYPE html>
<html lang="en">
<head>
<meta charset="utf-8">
<title>Keystone Facilities Services – Business Card</title>
<link rel="stylesheet" href="https://fonts.googleapis.com/css2?family=Cinzel:wght@600;700&display=swap">
<style>
  :root {
    --backdrop: #8e8889;
    --gold: #b5960f;
    --blue: #1b4c9c;
    --navy: #142a5c;
    --white: #ffffff;
    --snow-top: #dfe4ea;
    --snow-mid: #aab3bd;
    --grass: #6f9a3c;
    --grass-dark: #4d7429;
  }
  * { box-sizing: border-box; margin: 0; padding: 0; }
  html, body { width: 1200px; height: 661px; overflow: hidden; }
  body {
    background: var(--backdrop);
    font-family: "Cinzel", serif;
    position: relative;
  }
  .card {
    position: absolute;
    top: 176px;
    width: 540px;
    height: 309px;
    overflow: hidden;
    box-shadow: 0 6px 14px rgba(0,0,0,.25);
    background: var(--gold);
  }
  .card--front { left: 40px; }
  .card--back { left: 620px; }

  .front-band { position: absolute; inset: 0; }

  .brand {
    position: absolute;
    display: flex;
    flex-direction: column;
    align-items: center;
    color: var(--navy);
  }
  .brand__row { display: flex; align-items: center; gap: 8px; }
  .brand__dot {
    width: 18px; height: 18px; border-radius: 50%;
    background: var(--navy);
  }
  .brand__name { font-weight: 700; font-size: 30px; line-height: 1; }
  .brand__sub { font-weight: 700; font-size: 12px; line-height: 1.2; text-align: center; }

  .card--front .brand { left: 0; width: 540px; top: 50px; }

  .tagline {
    position: absolute;
    left: 0; width: 540px; top: 150px;
    text-align: center;
    font-weight: 700;
    font-size: 13.5px;
    letter-spacing: .5px;
    color: var(--white);
    -webkit-text-stroke: 3px var(--blue);
    paint-order: stroke fill;
  }
  .contact {
    position: absolute;
    left: 150px; width: 390px; top: 190px;
    text-align: center;
    color: var(--white);
    font-weight: 600;
    font-size: 15px;
    line-height: 1.8;
  }

  .photo { position: absolute; left: 0; top: 0; width: 540px; }
  .photo--winter {
    height: 150px;
    background: linear-gradient(180deg, var(--snow-top), var(--snow-mid));
  }
  .photo--summer {
    top: 150px; height: 145px; width: 370px;
    background: linear-gradient(180deg, var(--grass-dark), var(--grass));
  }
  .card--back .brand { right: 0; width: 170px; top: 182px; }
  .card--back .brand__row { gap: 6px; }
  .card--back .brand__dot { width: 14px; height: 14px; }
  .card--back .brand__name { font-size: 21px; }
  .card--back .brand__sub { font-size: 10px; }
</style>
</head>
<body>
  <section class="card card--front" aria-label="Card front">
    <svg class="front-band" width="540" height="309" viewBox="0 0 540 309" aria-hidden="true">
      <path d="M0 230 L130 230 Q138 180 170 178 L540 178 L540 309 L0 309 Z" fill="var(--blue)"/>
    </svg>
    <div class="brand">
      <div class="brand__row"><span class="brand__dot"></span><span class="brand__name">Keystone</span></div>
      <div class="brand__sub">Facilities Services<br>Halden, MA</div>
    </div>
    <p class="tagline">Commercial and Industrial Property Maintenance</p>
    <div class="contact">
      <p>47 Brimwell Rd. Halden, Ma. 01472</p>
      <p>978-552-7314</p>
    </div>
  </section>

  <section class="card card--back" aria-label="Card back">
    <div class="photo photo--winter" role="img" aria-label="Photo of a wheel loader clearing snow beside snowy trees"></div>
    <div class="photo photo--summer" role="img" aria-label="Photo of a ride-on mower on a green lawn"></div>
    <div class="brand">
      <div class="brand__row"><span class="brand__dot"></span><span class="brand__name">Keystone</span></div>
      <div class="brand__sub">Facilities Services<br>Halden, MA</div>
    </div>
  </section>
</body>
</html>
```